ALL ASPECTS OF PLASTERING INC: TEXTURE,SANDFINISH RENO,POOLS, PATCH WORK ( STATEWIDE SERVICE GOOD RATES) 100% GUARANTEED FULLY INSURED C

Target Market(s)

ANYONE WHO OWNS A HOUSE,BUILDERS

Industry/Entity Type

Work

Contact Information for Business Card

GRITT-WALL PLASTERING SERVICES
BERNARD KOVALEC 0438259164
EMAIL:TARVEK48@QUILLMAIL.COM

Requirements
Must have
• COLOUR BACKGROUND WIV PLASTERING PICTURE EG TROWEL, CEMENT MIXER, SAND
Nice to have
• BOLD PROFESSIONAL LOOKING AND SOUNDING CATCHY SAYING
Should not have
• FLURO COLOURS

```html
<!DOCTYPE html>
<html lang="en">
<head>
<meta charset="utf-8">
<title>Gritt-Wall Plastering Services – Business Card</title>
<link rel="stylesheet" href="https://fonts.googleapis.com/css2?family=Lilita+One&family=Federo&family=Open+Sans:wght@400&display=swap">
<style>
  :root {
    --brand-green: #16634e;
    --ink-teal: #1d5552;
    --band-grey: #cccccc;
    --paper: #ffffff;
  }
  html, body {
    margin: 0;
    padding: 0;
    width: 1200px;
    height: 741px;
    overflow: hidden;
    background: var(--paper);
  }
  .business-card {
    display: block;
    width: 1200px;
    height: 741px;
  }
  .card-background { fill: var(--paper); }
  .accent-bar { fill: var(--brand-green); }
  .contact-band { fill: var(--band-grey); }
  .company-name {
    font-family: "Lilita One", "Arial Black", sans-serif;
    font-size: 56px;
    fill: var(--brand-green);
  }
  .service-list {
    font-family: "Open Sans", Arial, sans-serif;
    font-weight: 400;
    font-size: 30px;
    fill: var(--ink-teal);
  }
  .contact-details {
    font-family: "Federo", "Trebuchet MS", sans-serif;
    fill: var(--brand-green);
    stroke: var(--brand-green);
    stroke-width: 1.6px;
    stroke-linejoin: round;
    text-anchor: end;
  }
  .contact-name, .contact-phone { font-size: 47px; }
  .contact-email { font-size: 34px; stroke-width: 1.3px; }
</style>
</head>
<body>
<svg class="business-card" viewBox="0 0 1200 741" xmlns="http://www.w3.org/2000/svg" role="img" aria-label="Gritt-Wall Plastering Services business card">
  <rect class="card-background" x="0" y="0" width="1200" height="741"/>
  <rect class="contact-band" x="144" y="525" width="987" height="133"/>
  <rect class="accent-bar" x="70" y="82" width="74" height="576"/>

  <text class="company-name" x="160" y="146" textLength="769" lengthAdjust="spacingAndGlyphs">GRITT-WALL PLASTERING SERVICES</text>

  <g class="service-list">
    <text x="318" y="292" textLength="577" lengthAdjust="spacingAndGlyphs">ALL ASPECTS OF PLASTERING INCLUDING:</text>
    <text x="318" y="332" textLength="704" lengthAdjust="spacingAndGlyphs">TEXTURE, SANDFINISH RENO, POOLS, PATCH WORK</text>
    <text x="318" y="369" textLength="489" lengthAdjust="spacingAndGlyphs">( STATEWIDE SERVICE GOOD RATES)</text>
    <text x="318" y="408" textLength="649" lengthAdjust="spacingAndGlyphs">100% GUARANTEED FULLY INSURED COMPANY</text>
  </g>

  <g class="contact-details">
    <text class="contact-name" x="1129" y="563" textLength="458" lengthAdjust="spacingAndGlyphs">BERNARD KOVALEC</text>
    <text class="contact-phone" x="1129" y="614" textLength="252" lengthAdjust="spacingAndGlyphs">0438259164</text>
    <text class="contact-email" x="1129" y="655" textLength="620" lengthAdjust="spacingAndGlyphs">EMAIL:TARVEK48@QUILLMAIL.COM</text>
  </g>
</svg>
</body>
</html>
```